Bref créative
Solo Practice Attorney Biz Cards & Stationery
Biz Cards and Stationery for Solo Practice
Professional
Thomas R. Halvorsen
Attorney At Law
Two Cedar Court
247 N.W. Ninth Street, Suite 2306
Fort Lauderdale, FL 33271
thomas@halvorsenlegalgroup.com
www.halvorsenlegalgroup.com
I would like to see several different ideas for business cards, stationery, and the like. I believe my logo reflects a professional, modern, yet modest character. I would like my other project materials to do the same. I will comment and offer suggestions as the project continues. Many thanks.
Ok, designers: I would like to put a QR Code on the back of the business card that links directly to my website. Does anyone have experience with this? Let me see what you can do.

```html
<!DOCTYPE html>
<html lang="en">
<head>
<meta charset="utf-8">
<title>Halvorsen Legal Group — Stationery</title>
<link rel="stylesheet" href="https://fonts.googleapis.com/css2?family=Cormorant+Garamond:wght@500;600&family=Lato:wght@400;700&display=swap">
<style>
  :root {
    --stage: #2b2c2e;
    --paper: #ffffff;
    --navy: #1d3a6c;
    --ink: #5a5f66;
    --faint: #ececee;
    --shadow: rgba(0,0,0,.45);
  }
  * { box-sizing: border-box; margin: 0; padding: 0; }
  html, body { width: 1200px; height: 454px; overflow: hidden; }
  body { background: var(--stage); position: relative; font-family: "Lato", sans-serif; color: var(--ink); }
  .sheet { position: absolute; background: var(--paper); box-shadow: 0 3px 10px var(--shadow); overflow: hidden; }

  .wordmark { font-family: "Cormorant Garamond", serif; font-weight: 600; color: var(--navy);
    text-transform: uppercase; letter-spacing: .06em; line-height: 1; white-space: nowrap; display: flex; align-items: center; gap: .35em; }
  .wordmark .dot { width: .7em; height: .7em; background: var(--navy); display: inline-block; }
  .wordmark.light { color: #fff; }
  .wordmark.light .dot { background: #fff; }

  .tiny { font-size: 3.6px; line-height: 1.45; white-space: nowrap; }
  .tiny strong { color: var(--navy); font-weight: 700; }

  .watermark { position: absolute; left: 0; right: 0; text-align: center; font-family: "Cormorant Garamond", serif;
    font-weight: 600; color: var(--faint); letter-spacing: .04em; text-transform: uppercase; }

  /* business cards */
  .card { width: 113px; height: 64px; left: 79px; }
  .card-front { top: 91px; }
  .card-front .wordmark { position: absolute; left: 7px; top: 7px; font-size: 6px; }
  .card-front .tiny { position: absolute; left: 7px; top: 30px; }
  .card-info { top: 171px; }
  .card-info .wordmark { position: absolute; left: 7px; top: 6px; font-size: 6px; }
  .card-info .tiny { position: absolute; left: 7px; top: 20px; }
  .card-back { top: 251px; background: var(--navy); }
  .card-back .wordmark { position: absolute; left: 0; right: 0; top: 24px; justify-content: center; font-size: 7px; }
  .card-back .tag { position: absolute; left: 0; right: 0; top: 38px; text-align: center; font-size: 3.4px; letter-spacing: .2em; color: #cfd6e4; }

  /* letterheads */
  .letterhead { top: 41px; width: 278px; height: 365px; }
  .lh-one { left: 204px; }
  .lh-two { left: 515px; }
  .letterhead .wordmark { position: absolute; left: 20px; top: 16px; font-size: 9px; }
  .letterhead .watermark { top: 150px; font-size: 30px; }
  .lh-one .footer { position: absolute; left: 20px; right: 20px; bottom: 18px; display: flex; justify-content: space-between; }
  .lh-two .footer { position: absolute; left: 0; right: 0; bottom: 18px; text-align: center; }
  .lh-two .footer .row { display: flex; justify-content: center; gap: 7px; align-items: center; }
  .icon { width: 4px; height: 4px; display: inline-block; vertical-align: middle; margin-right: 1.5px; }

  /* envelopes */
  .envelope { left: 826px; width: 333px; height: 126px; }
  .env-front { top: 84px; }
  .env-front .wordmark { position: absolute; left: 14px; top: 14px; font-size: 8px; }
  .env-front .tiny { position: absolute; left: 14px; top: 28px; }
  .env-front .watermark { top: 30px; left: auto; right: 18px; font-size: 26px; text-align: right; }
  .env-back { top: 228px; }
  .env-back svg { position: absolute; inset: 0; }
  .env-back .wordmark { position: absolute; left: 0; right: 0; top: 36px; justify-content: center; font-size: 7px; }
</style>
</head>
<body>

  <!-- business cards -->
  <section class="sheet card card-front" aria-label="Business card front">
    <div class="wordmark"><span class="dot"></span>Halvorsen Legal Group</div>
    <div class="tiny">
      <strong>Thomas R. Halvorsen</strong><br>
      Attorney At Law<br>
      T 954.555.0182 · F 954.555.0183<br>
      thomas@halvorsenlegalgroup.com
    </div>
  </section>

  <section class="sheet card card-info" aria-label="Business card details">
    <div class="wordmark"><span class="dot"></span>Halvorsen Legal Group</div>
    <div class="tiny">
      <strong>Thomas R. Halvorsen</strong><br>
      Attorney At Law<br>
      Two Cedar Court<br>
      247 N.W. Ninth Street, Suite 2306<br>
      Fort Lauderdale, FL 33271<br>
      T 954.555.0182 · F 954.555.0183<br>
      www.halvorsenlegalgroup.com
    </div>
  </section>

  <section class="sheet card card-back" aria-label="Business card back">
    <div class="wordmark light">Halvorsen</div>
    <div class="tag">ATTORNEY AT LAW</div>
  </section>

  <!-- letterheads -->
  <section class="sheet letterhead lh-one" aria-label="Letterhead, left-aligned footer">
    <div class="wordmark"><span class="dot"></span>Halvorsen Legal Group</div>
    <div class="watermark">Halvorsen</div>
    <div class="footer tiny">
      <span>Two Cedar Court · 247 N.W. Ninth Street, Suite 2306<br>Fort Lauderdale, FL 33271</span>
      <span>T 954.555.0182 · F 954.555.0183<br>www.halvorsenlegalgroup.com</span>
    </div>
  </section>

  <section class="sheet letterhead lh-two" aria-label="Letterhead, centred footer">
    <div class="watermark">Halvorsen</div>
    <div class="footer tiny">
      <div class="row">
        <span><svg class="icon" viewBox="0 0 10 10"><path d="M2 1h2l1 2.5-1.3 1a6 6 0 0 0 2.8 2.8l1-1.3L10 7v2c-5 .5-9.5-4-9-9z" fill="#1d3a6c"/></svg>954.555.0182</span>
        <span><svg class="icon" viewBox="0 0 10 10"><path d="M5 0a3.5 3.5 0 0 0-3.5 3.5C1.5 6 5 10 5 10s3.5-4 3.5-6.5A3.5 3.5 0 0 0 5 0zm0 5a1.5 1.5 0 1 1 0-3 1.5 1.5 0 0 1 0 3z" fill="#1d3a6c"/></svg>247 N.W. Ninth Street, Suite 2306, Fort Lauderdale, FL 33271</span>
      </div>
      <div class="row">thomas@halvorsenlegalgroup.com · www.halvorsenlegalgroup.com</div>
    </div>
  </section>

  <!-- envelopes -->
  <section class="sheet envelope env-front" aria-label="Envelope front">
    <div class="wordmark"><span class="dot"></span>Halvorsen Legal Group</div>
    <div class="tiny">
      Two Cedar Court<br>
      247 N.W. Ninth Street, Suite 2306<br>
      Fort Lauderdale, FL 33271
    </div>
    <div class="watermark">Halvorsen</div>
  </section>

  <section class="sheet envelope env-back" aria-label="Envelope back">
    <svg width="333" height="126" viewBox="0 0 333 126" aria-hidden="true">
      <path d="M0 0H333V12L185 62Q166.5 68 148 62L0 12Z" fill="var(--navy)"/>
      <path d="M0 126L150 70Q166.5 64 183 70L333 126" fill="none" stroke="#e3e4e7" stroke-width=".8"/>
    </svg>
    <div class="wordmark light">Halvorsen</div>
  </section>

</body>
</html>
```